New local Orchid nursery branding

We need a business card designed for our small local company in Darwin, Australia that grows orchids, called Blooms at Carrow.
We will be running private sales from our property, and handing these out at local events for perspective customers.

We would like to see designs that are simple, and able to be used with minimal colours and containing an orchid, preferably a stylised representation instead of a photo.
The eventual hope is to take this into larger formats to create our company logo/branding etc, but for now we just need business cards.

Target Market(s)

Local Orchid

Industry/Entity Type

Business

Contact Information for Business Card

Company Name
Logo
Name
Phone Number
Street Address
Email Address (less prominent than rest of the text)

Font styles to use
Sans Serif

Requirements
Must have
• Name of the company, which is Blooms at Carrow
Nice to have
• stylised orchid logo
Should not have
• too many colours

```html
<!DOCTYPE html>
<html lang="en">
<head>
<meta charset="utf-8">
<title>Blooms at Carrow — Business Card</title>
<link rel="stylesheet" href="https://fonts.googleapis.com/css2?family=Arimo:wght@400;700&display=swap">
<style>
  :root {
    --page-bg: #ececec;
    --card-white: #ffffff;
    --card-grey: #e4e4e4;
    --frame-line: #1a1a1a;
    --ink: #111111;
    --ink-soft: #333333;
    --brand-blue: #3b4cb0;
    --title-blue: #4a55c4;
  }
  * { margin: 0; padding: 0; box-sizing: border-box; }
  html, body {
    width: 1200px; height: 900px; overflow: hidden;
    background: var(--page-bg);
    font-family: "Arimo", Arial, sans-serif;
  }
  .canvas {
    width: 1200px; height: 900px;
    display: flex; align-items: center; justify-content: center;
  }
  .business-card {
    position: relative;
    width: 900px; height: 515px;
    background: linear-gradient(120deg, var(--card-white) 25%, var(--card-grey) 100%);
    box-shadow: 0 6px 24px rgba(0,0,0,0.18);
  }
  .card-frame {
    position: absolute; inset: 22px;
    border: 1.5px solid var(--frame-line);
  }
  .card-content {
    position: absolute; inset: 22px;
    display: flex; flex-direction: column; align-items: center; justify-content: center;
    text-align: center; color: var(--ink);
  }
  .brand-lockup {
    display: flex; align-items: center; gap: 16px;
    margin-bottom: 30px;
  }
  .brand-dot {
    width: 34px; height: 34px; border-radius: 50%;
    background: var(--brand-blue);
  }
  .brand-name {
    font-size: 46px; font-weight: 700; color: var(--brand-blue);
    letter-spacing: 0.5px;
  }
  .person-name { font-size: 44px; font-weight: 400; line-height: 1.1; }
  .person-title { font-size: 19px; color: var(--title-blue); margin: 6px 0 20px; }
  .contact-line { font-size: 21px; line-height: 1.55; }
  .contact-email { font-size: 19px; color: var(--ink-soft); }
</style>
</head>
<body>
  <main class="canvas">
    <section class="business-card">
      <div class="card-frame"></div>
      <div class="card-content">
        <div class="brand-lockup">
          <span class="brand-dot"></span>
          <span class="brand-name">Blooms at Carrow</span>
        </div>
        <p class="person-name">Your name here</p>
        <p class="person-title">Title here</p>
        <p class="contact-line">Address here, Address here, Address here</p>
        <p class="contact-line">0391-5567-2480</p>
        <p class="contact-line contact-email">hello@bloomsatcarrow.net</p>
      </div>
    </section>
  </main>
</body>
</html>
```